Homebuilder & Remodeling Firm looking for archectrual looking website

We are a Custom home building & remodeling company since 1986 and would like to launch a website.Carl Tondevik the principle of the firm is a graduate of Harwell Univesity school of architecture and draws his own designs and working drawings. and has done many residential, single and multi family projects in the Dallas Ft Worth Metroplex. We want our website to be architectural in design and visually appealing. We will eventually have photos to provide for you. The message we want to communicate is we have current update knowledge with trends, and longevity in experience. Our message is that we are a firm that designs and remodels fully through and we provide a well executed custom home that is unique to each client. The Homes that we build are unique ,authentic and sustainable architectural styles such as mid century modern, contemporary, transitional and they are sophisticated homes to compliment individual lifestyles of our clients. We have a passion for construction and an attention to detail that makes your dreams come to life. We listen to each clients every need in functionality and form and take them from pre-construction to post-construction follow -up.
We help you invest in your home. Thoughts Create Reality

EXAMPLES OF WEBSITES THAT WE LIKE. PLEASE DO
MORE CONTEMPORARY, SLEEK, ARCHITECTURAL

* Please make the LOGO a bigger part of design

http://pellamcrew.build/
https://www.vintrasol.co/
http://dostavanehomes.com/
http://www.milesfardowdesign.com/
http://www.quillmerton.com/
http://fennikdesignstudios.com/about
http://brandelorgc.com/

thank you,

Reason: We have many clients asking to see our website and re ready to launch something for them to look at

Target Market(s)

Home owners, home buyers, interior designers, All ages

Industry/Entity Type

Builders

Coding

Coded - Design and coding required

Number of Pages Required

5+ page

Font styles to use
Sans Serif

Requirements
Must have
• HTML5 OR PHP
• graphic artist must speak English:
• *Visually appealing, user friendly,
• * the website should reflect the stability and integrity of the company since it has been in business for over 30 years
• * a sophistication and refinement is our mandate.
Should not have
• Too busy, too much going on, we want more minimal in design and artsitic

```html
<!DOCTYPE html>
<html lang="en">
<head>
<meta charset="utf-8">
<title>Tondevik Development — Custom Homes &amp; Remodeling</title>
<link href="https://fonts.googleapis.com/css2?family=Roboto:wght@300;400;500;700&family=Open+Sans:wght@400;600;700&display=swap" rel="stylesheet">
<style>
:root{
  --navy:#1d3557;
  --blue:#1f5aa6;
  --blue-link:#2a5fa8;
  --ink:#333;
  --muted:#8a8a8a;
  --line:#e3e3e3;
  --soft:#f4f4f4;
  --dark:#1b1b1b;
  --white:#fff;
}
*{margin:0;padding:0;box-sizing:border-box}
html,body{width:1200px;height:2643px;overflow:hidden;background:var(--white)}
body{font-family:"Open Sans",Arial,sans-serif;color:var(--ink);position:relative}
section,header,nav,footer{position:absolute;left:0;width:1200px}
.abs{position:absolute}

/* header */
.site-header{top:0;height:109px}
.brand{left:132px;top:26px;display:flex;align-items:center;gap:14px}
.brand-mark{width:40px;height:58px;background:var(--navy)}
.brand-name{font-family:"Roboto",sans-serif;font-weight:400;font-size:30px;color:var(--navy);letter-spacing:.2px}
.phone{left:802px;top:34px;display:flex;align-items:center;gap:12px;font-size:12px;color:#555}
.phone-icon{width:38px;height:38px;border:1px solid #bbb;border-radius:50%;display:flex;align-items:center;justify-content:center}
.phone strong{font-size:17px;color:#222;font-weight:600}
.header-divider{left:1033px;top:30px;width:1px;height:48px;background:var(--line)}
.search{left:1046px;top:42px}

/* nav */
.main-nav{top:109px;height:53px;border-top:1px solid var(--line);background:#fafafa}
.main-nav a{position:absolute;top:0;height:53px;line-height:53px;font-size:12px;color:#444;text-decoration:none;text-transform:uppercase;transform:translateX(-50%)}
.main-nav a.active{width:108px;text-align:center;background:var(--white);color:var(--blue);font-weight:700;border-bottom:3px solid var(--blue);border-left:1px solid var(--line);border-right:1px solid var(--line)}

/* hero */
.hero{top:162px;height:532px;background:linear-gradient(90deg,#a4683a 0%,#c7a07a 25%,#d9cfc2 45%,#cfcac4 65%,#9d9b98 100%)}
.hero-floor{left:0;bottom:0;width:1200px;height:230px;background:linear-gradient(180deg,rgba(210,205,198,.0),#cbc7c2)}
.hero-badge{left:675px;top:49px;width:388px;height:388px;border-radius:50%;background:rgba(24,82,160,.82);text-align:center;color:var(--white)}
.hero-badge::after{content:"";position:absolute;inset:10px;border:1px solid rgba(255,255,255,.6);border-radius:50%}
.hero-kicker{margin-top:96px;font-family:"Roboto",sans-serif;font-weight:300;font-size:25px;letter-spacing:1px}
.hero-title{font-family:"Roboto",sans-serif;font-weight:700;font-size:40px;letter-spacing:1px;margin-top:6px}
.hero-text{font-size:16px;line-height:30px;margin:14px auto 0;width:320px;opacity:.9}
.hero-btn{display:inline-block;margin-top:24px;padding:10px 18px;border:1px solid var(--white);font-size:12px;font-weight:700;position:relative;z-index:1}
.slider-arrow{top:450px;width:26px;height:26px;border-radius:50%;background:#666;display:flex;align-items:center;justify-content:center}

/* services */
.services{top:694px;height:397px}
.section-title{width:1200px;text-align:center;font-family:"Roboto",sans-serif;font-weight:300;font-size:33px;color:#333}
.section-lead{left:300px;width:600px;text-align:center;font-size:12px;line-height:24px;color:#777}
.service{top:213px;width:310px;display:flex;gap:20px}
.service-icon{flex:none;width:88px;height:88px;border:1px solid #999;border-radius:50%;display:flex;align-items:center;justify-content:center}
.service h3{font-family:"Open Sans",sans-serif;font-weight:400;font-size:14px;color:var(--blue-link);margin:6px 0 10px}
.service p{font-size:11px;line-height:22px;color:#888}
.service-divider{top:193px;width:1px;height:130px;background:var(--line)}

/* welcome */
.welcome{top:1091px;height:410px;background:linear-gradient(90deg,#1a1a1a,#2a2a2a 50%,#151515)}
.welcome h2{left:132px;top:64px;font-family:"Roboto",sans-serif;font-weight:300;font-size:32px;color:var(--white)}
.welcome p{left:132px;width:450px;font-size:11px;line-height:23px;color:#ddd}
.btn-outline{left:132px;top:288px;padding:8px 14px;border:2px solid var(--white);color:var(--white);font-size:11px;font-weight:700;display:flex;align-items:center;gap:10px}
.video{left:629px;top:63px;width:439px;height:270px;background:var(--white)}
.video-frame{left:0;top:0;width:439px;height:244px;background:linear-gradient(120deg,#f1ece4,#d8c4a2 55%,#9b6a3d)}
.play{left:191px;top:94px;width:54px;height:54px;border-radius:50%;background:rgba(30,30,30,.8);border:2px solid var(--white)}
.controls{left:0;top:244px;width:439px;height:26px;display:flex;align-items:center;gap:10px;padding:0 12px;font-size:8px;color:#444}
.track{width:196px;height:3px;background:#ccc;position:relative}
.track::before{content:"";position:absolute;left:0;top:0;width:90px;height:3px;background:#e0503d}
.vol{width:28px;height:3px;background:#e0503d}

/* projects */
.projects{top:1501px;height:513px;background:var(--soft)}
.project{top:146px;width:211px;height:286px;background:var(--white);box-shadow:0 1px 3px rgba(0,0,0,.08);text-align:center;padding:4px}
.project-photo{width:203px;height:158px}
.project h3{font-size:11px;font-weight:700;color:var(--navy);margin-top:16px;text-transform:uppercase}
.project p{font-size:11px;line-height:20px;color:#888;margin-top:8px}
.project a{display:inline-block;margin-top:8px;font-size:11px;color:#333;text-decoration:underline}

/* testimonials */
.testimonials{top:2014px;height:386px}
.quote{top:150px;width:420px;padding-left:0}
.quote p{font-size:11px;line-height:23px;color:#777}
.quote p::before{content:"\201C";font-family:Georgia,serif;font-size:24px;color:#555;margin-right:4px;vertical-align:-6px}
.quote-rule{top:143px;width:1px;height:170px;background:var(--line)}
.author{display:flex;align-items:center;gap:18px;margin-top:22px}
.avatar{width:70px;height:70px;border-radius:50%;background:linear-gradient(160deg,#d9dbdd,#a9adb2)}
.author-name{font-size:12px;color:#555;text-transform:uppercase;margin-bottom:10px}
.rating{display:flex;align-items:center;gap:8px;font-size:12px;color:var(--blue-link);font-style:italic}
.stars{display:flex;gap:1px}
.star{width:14px;height:14px;background:var(--blue);display:flex;align-items:center;justify-content:center}

/* footer */
.site-footer{top:2400px;height:243px;background:#f6f6f6;border-top:3px solid var(--blue)}
.footer-brand{left:132px;top:58px}
.social{left:192px;top:122px;display:flex;gap:6px}
.social span{width:24px;height:24px;border-radius:50%;background:var(--blue-link)}
.copyright{left:166px;top:170px;font-size:10px;color:#666}
.footer-divider{left:436px;top:40px;width:1px;height:170px;background:#ddd}
.footer-heading{font-size:13px;color:#333;text-transform:uppercase}
.contact-item{left:497px;display:flex;gap:12px;font-size:11px;color:#666;line-height:20px}
.newsletter input,.field{position:absolute;left:822px;width:246px;height:37px;background:var(--white);border:1px solid #e6e6e6;font-size:10px;padding-left:12px;line-height:37px;color:#333}
.subscribe{left:975px;top:130px;width:93px;height:37px;background:#1a1a1a;color:var(--white);font-size:11px;font-weight:700;line-height:37px;text-align:center}
</style>
</head>
<body>

<header class="site-header">
  <div class="brand abs">
    <span class="brand-mark"></span>
    <span class="brand-name">Tondevik Development</span>
  </div>
  <div class="phone abs">
    <span class="phone-icon">
      <svg width="16" height="16" viewBox="0 0 24 24" fill="none" stroke="#666" stroke-width="1.6"><path d="M5 3h4l2 5-2.5 1.5a11 11 0 0 0 6 6L16 13l5 2v4a2 2 0 0 1-2 2A17 17 0 0 1 3 5a2 2 0 0 1 2-2z"/></svg>
    </span>
    <span>PHONE : <strong>(+345) 555-0142</strong></span>
  </div>
  <span class="header-divider abs"></span>
  <svg class="search abs" width="22" height="22" viewBox="0 0 24 24" fill="none" stroke="#555" stroke-width="1.6"><circle cx="10" cy="10" r="7"/><path d="M15 15l6 6"/></svg>
</header>

<nav class="main-nav">
  <a class="active" href="#" style="left:186px">Home</a>
  <a href="#" style="left:312px">About</a>
  <a href="#" style="left:455px">Services</a>
  <a href="#" style="left:596px">Projects</a>
  <a href="#" style="left:731px">Blog</a>
  <a href="#" style="left:879px">Testimonials</a>
  <a href="#" style="left:1040px">Contact</a>
</nav>

<section class="hero" role="img" aria-label="Photo of a bright remodeled kitchen and living room with wood cabinets and carpet">
  <div class="hero-floor abs"></div>
  <div class="hero-badge abs">
    <div class="hero-kicker">RESIDENTIAL</div>
    <div class="hero-title">REMODELING</div>
    <p class="hero-text">Eiusmod tempor incididunt ut labore et dolore magna aliqua enim ad minim...</p>
    <span class="hero-btn">VIEW MORE INFORMATION</span>
  </div>
  <span class="slider-arrow abs" style="left:132px"><svg width="10" height="10" viewBox="0 0 10 10"><path d="M6.5 1.5L3 5l3.5 3.5" stroke="#fff" stroke-width="1.6" fill="none"/></svg></span>
  <span class="slider-arrow abs" style="left:165px"><svg width="10" height="10" viewBox="0 0 10 10"><path d="M3.5 1.5L7 5 3.5 8.5" stroke="#fff" stroke-width="1.6" fill="none"/></svg></span>
</section>

<section class="services">
  <h2 class="section-title abs" style="top:64px">Our Services</h2>
  <p class="section-lead abs" style="top:112px">Accusantium doloremque laudantium, totam rem aperiam, eaque ipsa quae ab illo inventore veritatis et quasi architecto beatae vitae quia voluptas</p>

  <div class="service abs" style="left:132px">
    <span class="service-icon"><svg width="40" height="40" viewBox="0 0 40 40" fill="none" stroke="var(--blue)" stroke-width="1.6"><path d="M6 20L20 8l14 12"/><path d="M10 17v16h20V17"/><rect x="16" y="22" width="8" height="8"/><path d="M20 22v8M16 26h8"/></svg></span>
    <div><h3>Tempor Incididunt</h3><p>Aliquip ex ea commodo consequat. Duis aute irure dolor in reprehenderit in voluptate velit esse cillum...</p></div>
  </div>
  <span class="service-divider abs" style="left:439px"></span>
  <div class="service abs" style="left:455px">
    <span class="service-icon"><svg width="40" height="40" viewBox="0 0 40 40" fill="none" stroke="var(--blue)" stroke-width="1.6"><circle cx="20" cy="20" r="6"/><path d="M20 5v5M20 30v5M5 20h5M30 20h5M9.4 9.4l3.5 3.5M27.1 27.1l3.5 3.5M9.4 30.6l3.5-3.5M27.1 12.9l3.5-3.5"/><circle cx="20" cy="20" r="11"/></svg></span>
    <div><h3>Exercitation Allamco</h3><p>Aliquip ex ea commodo consequat. Duis aute irure dolor in reprehenderit in voluptate velit esse cillum...</p></div>
  </div>
  <span class="service-divider abs" style="left:765px"></span>
  <div class="service abs" style="left:781px">
    <span class="service-icon"><svg width="40" height="40" viewBox="0 0 40 40" fill="none" stroke="var(--blue)" stroke-width="1.6"><path d="M12 7h16v8a8 8 0 0 1-16 0z"/><path d="M12 10H7a5 5 0 0 0 5 7M28 10h5a5 5 0 0 1-5 7"/><path d="M20 23v6M14 34h12l-2-5h-8z"/></svg></span>
    <div><h3>Architecto Beatae</h3><p>Aliquip ex ea commodo consequat. Duis aute irure dolor in reprehenderit in voluptate velit esse cillum...</p></div>
  </div>
</section>

<section class="welcome">
  <h2 class="abs">Welcome Tondevik Development</h2>
  <p class="abs" style="top:124px">Sed ut perspiciatis unde omnis iste natus error sit voluptatem accusantium doloremque laudantium, totam rem aperiam, eaque ipsa quae ab illo inventore veritatis et quasi voluptas sit aspernatur aut odit aut fugit, sed quia consequuntur...</p>
  <p class="abs" style="top:200px">Sed ut perspiciatis unde omnis iste natus error sit voluptatem accusantium doloremque laudantium, totam rem aperiam, eaque ipsa quae ab illo inventore veritatis et quasi architecto beatae vitae dicta sunt explicabo...</p>
  <span class="btn-outline abs">MORE VIDEOS <svg width="10" height="10" viewBox="0 0 10 10"><path d="M3 1l4 4-4 4" stroke="#fff" stroke-width="1.8" fill="none"/></svg></span>
  <div class="video abs">
    <div class="video-frame abs" role="img" aria-label="Video still of a bright kitchen with a white island and wood floor"></div>
    <span class="play abs"><svg width="50" height="50" viewBox="0 0 50 50"><path d="M20 15l15 10-15 10z" fill="#fff"/></svg></span>
    <div class="controls abs">
      <svg width="8" height="8" viewBox="0 0 8 8"><path d="M1 0l7 4-7 4z" fill="#333"/></svg>
      <span>10:00/05:03</span>
      <span class="track"></span>
      <span style="flex:1"></span>
      <svg width="10" height="9" viewBox="0 0 10 9"><path d="M0 3h3l3-3v9L3 6H0z" fill="#333"/></svg>
      <span class="vol"></span>
    </div>
  </div>
</section>

<section class="projects">
  <h2 class="section-title abs" style="top:76px">Our Projects</h2>
  <article class="project abs" style="left:132px">
    <div class="project-photo" role="img" aria-label="Photo of a dark wood kitchen with granite island" style="background:linear-gradient(135deg,#3a2a20,#8b6a4c 60%,#d8c6a8)"></div>
    <h3>Totam Rem Aperiam</h3><p>Speriam, eaque ipsa quae inven veritatis architecto...</p><a href="#">Click View More Information!</a>
  </article>
  <article class="project abs" style="left:374px">
    <div class="project-photo" role="img" aria-label="Photo of a warm kitchen with red bar stools" style="background:linear-gradient(135deg,#a57a50,#d2b48c 55%,#b44a3a)"></div>
    <h3>Sequi Nesciunt</h3><p>Speriam, eaque ipsa quae inven veritatis architecto...</p><a href="#">Click View More Information!</a>
  </article>
  <article class="project abs" style="left:615px">
    <div class="project-photo" role="img" aria-label="Photo of a bedroom with coffered ceiling and patterned rug" style="background:linear-gradient(180deg,#efe6d6,#c9b08a 60%,#3e3a36)"></div>
    <h3>Eaque Ipsa</h3><p>Speriam, eaque ipsa quae inven veritatis architecto...</p><a href="#">Click View More Information!</a>
  </article>
  <article class="project abs" style="left:856px">
    <div class="project-photo" role="img" aria-label="Photo of a light kitchen with stainless range" style="background:linear-gradient(135deg,#d9c2a3,#b78a62 55%,#e9e2d8)"></div>
    <h3>Numquam Eius</h3><p>Speriam, eaque ipsa quae inven veritatis architecto...</p><a href="#">Click View More Information!</a>
  </article>
</section>

<section class="testimonials">
  <h2 class="section-title abs" style="top:74px">Testimonials</h2>
  <span class="quote-rule abs" style="left:132px"></span>
  <div class="quote abs" style="left:173px">
    <p>Aliquip ex ea commodo consequat. Duis aute irure dolor in reprehenderit in voluptate velit esse cillum dolore eu fugiat nulla pariatur. Excepteur occaecat cupidatat non proident, sunt in culpa qui officia deserunt mollit...</p>
    <div class="author">
      <span class="avatar" role="img" aria-label="Portrait of the client"></span>
      <div><div class="author-name">-Dale Mercer</div>
        <div class="rating"><span class="stars"><i class="star"></i><i class="star"></i><i class="star"></i><i class="star"></i><i class="star"></i></span>(88 reviews)</div></div>
    </div>
  </div>
  <span class="quote-rule abs" style="left:646px"></span>
  <div class="quote abs" style="left:687px">
    <p>Aliquip ex ea commodo consequat. Duis aute irure dolor in reprehenderit in voluptate velit esse cillum dolore eu fugiat nulla pariatur. Excepteur occaecat cupidatat non proident, sunt in culpa qui officia deserunt mollit...</p>
    <div class="author">
      <span class="avatar" role="img" aria-label="Portrait of the client"></span>
      <div><div class="author-name">-Dale Mercer</div>
        <div class="rating"><span class="stars"><i class="star"></i><i class="star"></i><i class="star"></i><i class="star"></i><i class="star"></i></span>(88 reviews)</div></div>
    </div>
  </div>
</section>

<footer class="site-footer">
  <div class="brand footer-brand abs">
    <span class="brand-mark" style="width:34px;height:50px"></span>
    <span class="brand-name" style="font-size:26px">Tondevik Development</span>
  </div>
  <div class="social abs"><span></span><span></span><span></span><span></span><span></span></div>
  <p class="copyright abs">Copyrights©Tondevik Development 2017</p>
  <span class="footer-divider abs"></span>

  <h4 class="footer-heading abs" style="left:497px;top:44px">Contact Us</h4>
  <div class="contact-item abs" style="top:82px">
    <svg width="12" height="14" viewBox="0 0 12 14" style="margin-top:4px"><path d="M6 0a5 5 0 0 1 5 5c0 4-5 9-5 9S1 9 1 5a5 5 0 0 1 5-5z" fill="#888"/><circle cx="6" cy="5" r="2" fill="#f6f6f6"/></svg>
    <span>Tondevik Development P.O. Box 2170<br>Street Name,City-5333</span>
  </div>
  <div class="contact-item abs" style="top:138px">
    <svg width="12" height="12" viewBox="0 0 24 24" style="margin-top:4px"><path d="M5 3h4l2 5-2.5 1.5a11 11 0 0 0 6 6L16 13l5 2v4a2 2 0 0 1-2 2A17 17 0 0 1 3 5a2 2 0 0 1 2-2z" fill="#888"/></svg>
    <span style="font-size:13px">Phone: (+345) 555-0142</span>
  </div>
  <div class="contact-item abs" style="top:180px">
    <svg width="12" height="10" viewBox="0 0 12 10" style="margin-top:5px"><rect width="12" height="10" fill="#888"/><path d="M0 0l6 5 6-5" stroke="#f6f6f6" fill="none"/></svg>
    <span>Email: info@tondevikdevelopment.com</span>
  </div>

  <h4 class="footer-heading abs" style="left:822px;top:44px">Sign up for Newsletter</h4>
  <span class="field" style="top:80px">Enter Name</span>
  <span class="field" style="top:130px">Enter Email</span>
  <span class="subscribe abs">SUBSCRIBE</span>
</footer>

</body>
</html>
```